Brovik Kitchen Layout Design, packaging fonts and layout

UPDATE 8/3: Please see new update here: https://fileshare-demo.example/t-mLpQwZ7rTb
UPDATE: Please find updated instructions (BROVIK UPDATE2.pdf) in link below.
Brovik is a reputable housewares kitchen brand that has been in the market for over two decades. We are looking to update our packaging with new typeface(s) and update the packaging layout. Instructions and source art files can be found here:
https://fileshare-demo.example/t-HvNd3KxYuE
Updates

Please see new update here: https://fileshare-demo.example/t-mLpQwZ7rTb

Target Market(s)

Housewares

Industry/Entity Type

Housewares

Font styles to use
Sans Serif

Colors
00AB8E
00BBA5
67D7C9
C6EFE9
E9F9F6

Requirements
Must have
• New typefaces and layout. Design should have a hint of red, possibly in the form of an icon.
Nice to have
• Looking for a traditional, classic design with a modern twist! I would like to see options for the the top of the Pasta Machine box.

```html
<!DOCTYPE html>
<html lang="en">
<head>
<meta charset="utf-8">
<title>Brovik Pasta Machine – Box Top</title>
<link rel="stylesheet" href="https://fonts.googleapis.com/css2?family=Barlow+Semi+Condensed:wght@500&family=Barlow+Condensed:wght@500&family=Jost:wght@400&display=swap">
<style>
  :root {
    --teal-deep: #00AB8E;
    --teal-bright: #00BBA5;
    --teal-soft: #67D7C9;
    --teal-pale: #C6EFE9;
    --teal-mist: #E9F9F6;
    --ink-teal: #0b5e52;
    --shadow-teal: rgba(0, 70, 60, 0.55);
    --flag-green: #1d5a2a;
    --flag-white: #ffffff;
    --flag-red: #c8161d;
    --type-white: #ffffff;
    --steel-light: #f2f3f4;
    --steel-mid: #c3c7cb;
    --steel-dark: #8d9297;
  }
  * { margin: 0; padding: 0; box-sizing: border-box; }
  html, body { width: 1200px; height: 767px; overflow: hidden; background: var(--teal-mist); }
  .box-top { position: relative; width: 1200px; height: 767px; background: var(--teal-mist); overflow: hidden; }

  .hero-band {
    position: absolute; left: 0; top: 94px; width: 1200px; height: 524px;
    background: linear-gradient(90deg, var(--teal-deep), var(--teal-bright) 50%, var(--teal-deep));
  }
  .hero-band-rule {
    position: absolute; left: 0; top: 618px; width: 1200px; height: 8px; background: var(--teal-soft);
  }

  .flag-ribbon { position: absolute; left: 885px; }
  .flag-ribbon--top { top: 0; }
  .flag-ribbon--bottom { top: 450px; }

  .product-shot {
    position: absolute; left: 46px; top: 66px; width: 600px; height: 600px;
    border-radius: 18px;
    background: radial-gradient(ellipse at 40% 40%, var(--steel-light), var(--steel-mid) 55%, var(--steel-dark));
  }

  .title-line {
    position: absolute; left: 672px; width: 490px;
    text-align: center; white-space: nowrap; color: var(--type-white); line-height: 1;
  }
  .title-kicker {
    top: 146px;
    font-family: "Barlow Semi Condensed", sans-serif; font-weight: 500;
    font-size: 40px; letter-spacing: 3px;
  }
  .title-main {
    font-family: "Jost", sans-serif; font-weight: 400;
    text-shadow: 3px 3px 0 var(--shadow-teal);
  }
  .title-main--pasta { top: 180px; font-size: 150px; letter-spacing: 2px; }
  .title-main--machine { top: 330px; font-size: 94px; letter-spacing: 1px; }

  .brand-lockup {
    position: absolute; left: 735px; top: 478px; width: 370px; height: 124px;
    display: flex; align-items: center; justify-content: space-between;
  }
  .brand-lockup-word {
    font-family: "Barlow Semi Condensed", sans-serif; font-weight: 500;
    font-size: 22px; letter-spacing: 2.5px; color: var(--type-white);
  }
  .brand-seal {
    width: 124px; height: 124px; border-radius: 50%;
    background: var(--teal-deep); border: 3px solid var(--type-white);
    display: flex; align-items: center; justify-content: center;
    font-family: "Barlow Semi Condensed", sans-serif; font-weight: 500;
    font-size: 24px; letter-spacing: 2px; color: var(--type-white);
  }

  .feature-line {
    position: absolute; left: 480px; top: 676px; width: 680px; text-align: right; white-space: nowrap;
    font-family: "Barlow Condensed", sans-serif; font-weight: 500;
    font-size: 43px; color: var(--ink-teal); line-height: 1;
  }
</style>
</head>
<body>
<main class="box-top">
  <div class="hero-band"></div>
  <div class="hero-band-rule"></div>

  <svg class="flag-ribbon flag-ribbon--top" width="66" height="130" viewBox="0 0 66 130" aria-hidden="true">
    <rect x="0" y="0" width="22" height="130" fill="var(--flag-green)"/>
    <rect x="22" y="0" width="22" height="130" fill="var(--flag-white)"/>
    <rect x="44" y="0" width="22" height="130" fill="var(--flag-red)"/>
  </svg>

  <svg class="flag-ribbon flag-ribbon--bottom" width="66" height="198" viewBox="0 0 66 198" aria-hidden="true">
    <polygon points="0,0 22,0 22,186 0,198" fill="var(--flag-green)"/>
    <polygon points="22,0 44,0 44,186 33,180 22,186" fill="var(--flag-white)"/>
    <polygon points="44,0 66,0 66,198 44,186" fill="var(--flag-red)"/>
  </svg>

  <div class="product-shot" role="img" aria-label="Photo of a chrome hand-crank pasta machine with wooden handle and double spaghetti and fettuccine cutter"></div>

  <header>
    <p class="title-line title-kicker">GREAT AUNT TESSA’S</p>
    <h1 class="title-line title-main title-main--pasta">PASTA</h1>
    <p class="title-line title-main title-main--machine">MACHINE</p>
  </header>

  <div class="brand-lockup">
    <span class="brand-lockup-word">ITALIAN</span>
    <div class="brand-seal">BROVIK</div>
    <span class="brand-lockup-word">MARKET</span>
  </div>

  <p class="feature-line">with Double Spaghetti &amp; Fettucine Cutter</p>
</main>
</body>
</html>
```